Dale Morrikan Plumbing and Heating

Need a card design for a plumbing and heating company that does service and repair, remodels, and plumbing in new construction. Please add following on back side of card; Boilers, Water heaters, Gas lines, Sump pumps, Toilet repairs, Faucet repairs, Pipe thawing, Radiant heating, New construction, Remodels.

Industry/Entity Type

Plumber

Contact Information for Business Card

Was thinking white gloss card with colored logo in middle or black glossy card with silver logo in middle. Just a thought but very open to other designs.

Requirements
Must have
• Need following on front of card;
• P(203) 321-8689
• C(203) 232-9069
• Dale Morrikan 275 Larkwell Road, Harrowfield, VT 05214
• service@DrainHearth.example (plumbing in blue, heating in red)
• www.DrainHearth.example (plumbing in blue, heating in red)
• Fully Licensed and Insured
Nice to have
• Elegant design

```html
<!DOCTYPE html>
<html lang="en">
<head>
<meta charset="utf-8">
<title>Dale Morrikan Plumbing and Heating – Business Card</title>
<link rel="stylesheet" href="https://fonts.googleapis.com/css2?family=Exo+2:wght@700&family=Open+Sans:wght@400;600;700&display=swap">
<style>
  :root {
    --bg: #d9d9da;
    --ink-black: #0b0b0d;
    --ink-dark: #1c1d21;
    --blue: #1f63b5;
    --blue-bright: #2a8ee0;
    --blue-deep: #0f3f86;
    --red: #d3262f;
    --grey-text: #555a60;
    --white: #ffffff;
    --silver: #b9bcc2;
    --rule: #6b6e74;
  }
  * { box-sizing: border-box; margin: 0; padding: 0; }
  html, body { width: 1200px; height: 852px; overflow: hidden; }
  body {
    background: var(--bg);
    font-family: "Open Sans", Arial, sans-serif;
    display: flex;
    align-items: center;
    justify-content: center;
    gap: 40px;
  }
  .card {
    position: relative;
    width: 560px;
    height: 320px;
    border-radius: 18px;
    overflow: hidden;
    box-shadow: 0 6px 18px rgba(0,0,0,.25);
  }

  /* ---------- Brand name ---------- */
  .brand {
    font-family: "Open Sans", Arial, sans-serif;
    font-weight: 700;
    text-transform: uppercase;
    letter-spacing: 2px;
    display: flex;
    align-items: center;
    gap: 12px;
  }
  .brand__dot { width: 30px; height: 30px; border-radius: 50%; flex: none; }

  /* ---------- Back ---------- */
  .card--back {
    background: linear-gradient(160deg, var(--ink-dark) 0%, var(--ink-black) 60%);
  }
  .card--back .brand {
    position: absolute;
    top: 46px; left: 0; right: 0;
    justify-content: center;
    color: var(--silver);
    font-size: 22px;
    line-height: 1.15;
  }
  .card--back .brand__dot { background: var(--silver); }
  .services {
    position: absolute;
    left: 0; right: 0;
    top: 150px;
    height: 106px;
    background: linear-gradient(90deg, var(--blue-deep) 0%, var(--blue) 45%, var(--blue-bright) 100%);
    display: flex;
    flex-direction: column;
    justify-content: center;
    align-items: center;
    gap: 2px;
    font-family: "Exo 2", Arial, sans-serif;
    font-weight: 700;
    font-size: 18px;
    letter-spacing: 1px;
    text-transform: uppercase;
    color: var(--white);
  }
  .services .sep { margin: 0 6px; }
  .web-line {
    position: absolute;
    left: 0; right: 0; bottom: 30px;
    display: flex;
    align-items: center;
    justify-content: center;
    gap: 14px;
    font-size: 13px;
    color: var(--silver);
  }
  .web-line::before, .web-line::after {
    content: "";
    width: 90px; height: 1px;
    background: var(--rule);
  }
  .hl-blue { color: var(--blue); }
  .hl-red { color: var(--red); }
  .web-line .hl-blue { color: var(--blue-bright); }

  /* ---------- Front ---------- */
  .card--front { background: var(--white); }
  .edge {
    position: absolute;
    left: 0; top: 0; bottom: 0;
    width: 46px;
    background: linear-gradient(180deg, var(--blue-bright), var(--blue-deep));
    border-right: 4px solid var(--red);
  }
  .card--front .brand {
    position: absolute;
    top: 36px; left: 80px;
    color: var(--blue);
    font-size: 20px;
    line-height: 1.15;
  }
  .card--front .brand__dot { background: var(--blue); }
  .person { position: absolute; left: 80px; top: 138px; }
  .person__name { font-size: 21px; font-weight: 600; color: var(--blue); }
  .person__role { font-size: 12px; color: var(--grey-text); }
  .contacts {
    position: absolute;
    left: 80px; top: 196px;
    list-style: none;
    font-size: 13.5px;
    color: var(--grey-text);
  }
  .contacts li { display: flex; align-items: center; gap: 10px; height: 21px; }
  .contacts svg { width: 14px; height: 14px; fill: var(--blue-deep); flex: none; }
  .contacts .no-icon { padding-left: 24px; }
  .licence {
    position: absolute;
    right: 30px; top: 120px;
    text-align: right;
    font-size: 14px;
    line-height: 1.35;
    color: var(--blue);
  }
</style>
</head>
<body>

  <section class="card card--back" aria-label="Card back">
    <div class="brand">
      <span class="brand__dot"></span>
      <span>Dale Morrikan<br>Plumbing and Heating</span>
    </div>
    <div class="services">
      <div>Boilers<span class="sep">•</span>Water Heaters<span class="sep">•</span>Gas Lines<span class="sep">•</span>Sump Pumps</div>
      <div>Toilet Repairs<span class="sep">•</span>Faucet Repairs<span class="sep">•</span>Pipe Thawing</div>
      <div>Radiant Heating<span class="sep">•</span>New Construction<span class="sep">•</span>Remodels</div>
    </div>
    <div class="web-line"><span>www.<span class="hl-blue">Drain</span><span class="hl-red">Hearth</span>.example</span></div>
  </section>

  <section class="card card--front" aria-label="Card front">
    <div class="edge"></div>
    <div class="brand">
      <span class="brand__dot"></span>
      <span>Dale Morrikan<br>Plumbing and Heating</span>
    </div>
    <p class="licence">Fully Licensed<br>and Insured</p>
    <div class="person">
      <p class="person__name">Dale Morrikan</p>
      <p class="person__role">Director</p>
    </div>
    <ul class="contacts">
      <li class="no-icon">(612) 555-0147</li>
      <li>
        <svg viewBox="0 0 16 16" aria-hidden="true"><path d="M3 2h3l1.5 3.5-2 1.2a8 8 0 0 0 3.8 3.8l1.2-2L14 10v3a1 1 0 0 1-1 1A11 11 0 0 1 2 3a1 1 0 0 1 1-1z"/></svg>
        <span>(612) 555-0183</span>
      </li>
      <li>
        <svg viewBox="0 0 16 16" aria-hidden="true"><path d="M4 1h8v4H4zM2 6h12a1 1 0 0 1 1 1v5h-3v3H4v-3H1V7a1 1 0 0 1 1-1zm3 5v3h6v-3z"/></svg>
        <span><span class="hl-blue">Drain</span><span class="hl-red">Hearth</span><span class="hl-blue">.example</span></span>
      </li>
      <li>
        <svg viewBox="0 0 16 16" aria-hidden="true"><path d="M8 1a7 7 0 1 0 0 14A7 7 0 0 0 8 1zm0 1.5c.8 0 1.7 1.6 2 3.8H6c.3-2.2 1.2-3.8 2-3.8zM2.6 7.3h2.3v1.4H2.6a5.5 5.5 0 0 1 0-1.4zm3.4 0h4v1.4H6zm5.1 0h2.3a5.5 5.5 0 0 1 0 1.4h-2.3zM6 9.7h4c-.3 2.2-1.2 3.8-2 3.8s-1.7-1.6-2-3.8z"/></svg>
        <span>service@<span class="hl-blue">Drain</span><span class="hl-red">Hearth</span>.example</span>
      </li>
      <li>
        <svg viewBox="0 0 16 16" aria-hidden="true"><path d="M1 3h14v10H1zm1.5 1.3v.4L8 8.6l5.5-3.9v-.4zM2.5 6.2v5.3h11V6.2L8 10.1z"/></svg>
        <span>275 Larkwell Road, Harrowfield, VT 05214</span>
      </li>
    </ul>
  </section>

</body>
</html>
```